New Business Cards for Organic Meat Farm

We need a business card designed for Thornbury Farm, a meat farm in western MA. Our logo uses a hand-drawn woodcut (attached). Our color palette has been simply black and white (shown in notepad and picture of our food truck). While we are based out of western MA, we have ambitions to grow nationally, so our hope is for a classy and memorable card which will be printed on a premium quality stock from a printer like printkestrel.com.
Target Market(s)
consumers of quality meats, restauranteurs, partnering farms
Industry/Entity Type
Farming and prepared meat products
Contact Information for Business Card
Wendell Pruitt, President/Owner, wendell@thornburyfarm.com, mobile: 413-555-0172, phone: 413-555-0148, thornburyfarm.com, facebook: @thornburyfarm, instagram: @thornburyfarmma
Colors
Designer to choose colors to be used in the design.
Look and feel

```html
<!DOCTYPE html>
<html lang="en">
<head>
<meta charset="utf-8">
<title>Quillmere Farm — Business Card</title>
<link href="https://fonts.googleapis.com/css2?family=Montserrat:wght@400;500;600&display=swap" rel="stylesheet">
<style>
  :root {
    --backdrop: #3b3b3b;
    --card: #0c0c0c;
    --silver: #cfcfcf;
    --silver-dim: #9a9a9a;
    --rule: #6d6d6d;
    --art-top: #8c8c8c;
    --art-bottom: #3a3a3a;
    --ghost-top: #262626;
    --ghost-bottom: #0f0f0f;
  }
  * { box-sizing: border-box; margin: 0; padding: 0; }
  html, body { width: 1200px; height: 2440px; overflow: hidden; }
  body {
    background: var(--backdrop);
    font-family: "Montserrat", sans-serif;
    color: var(--silver);
    display: flex;
    flex-direction: column;
    align-items: center;
    justify-content: center;
    gap: 80px;
  }
  .card {
    position: relative;
    width: 660px;
    height: 1100px;
    background: var(--card);
    border-radius: 36px;
    overflow: hidden;
    display: flex;
    flex-direction: column;
    align-items: center;
  }
  .farmhouse-art {
    position: relative;
    z-index: 2;
    margin-top: 70px;
    width: 400px;
    height: 200px;
    border-radius: 8px;
    background: linear-gradient(180deg, var(--art-top), var(--art-bottom));
  }
  .brand-name {
    position: relative;
    z-index: 2;
    margin-top: 26px;
    font-size: 72px;
    font-weight: 500;
    letter-spacing: 2px;
    color: var(--silver);
    line-height: 1;
  }
  .brand-sub {
    position: relative;
    z-index: 2;
    margin-top: 14px;
    font-size: 28px;
    font-weight: 500;
    letter-spacing: 10px;
    line-height: 1.2;
    color: var(--silver);
  }
  .person { position: relative; z-index: 2; margin-top: 80px; text-align: center; }
  .person-name {
    font-size: 44px;
    font-weight: 400;
    letter-spacing: 6px;
  }
  .person-rule {
    width: 300px;
    height: 2px;
    background: var(--rule);
    margin: 16px auto 12px;
  }
  .person-title {
    font-size: 24px;
    font-weight: 500;
    letter-spacing: 2px;
    color: var(--silver-dim);
  }
  .contact-list {
    position: relative;
    z-index: 2;
    list-style: none;
    align-self: flex-start;
    margin: 90px 0 0 48px;
    display: flex;
    flex-direction: column;
    gap: 12px;
  }
  .contact-item {
    display: flex;
    align-items: center;
    gap: 14px;
    font-size: 26px;
    letter-spacing: 1px;
  }
  .contact-icon { width: 26px; height: 26px; flex: none; }
  .social-row {
    position: absolute;
    z-index: 2;
    left: 48px;
    right: 40px;
    bottom: 46px;
    display: flex;
    gap: 36px;
    font-size: 20px;
    letter-spacing: 1px;
  }
  .social-handle { display: flex; align-items: center; gap: 10px; }
  .social-dot {
    width: 22px;
    height: 22px;
    border-radius: 50%;
    background: var(--silver);
  }
  .ghost-art {
    position: absolute;
    z-index: 1;
    left: 0;
    right: 0;
    bottom: 0;
    height: 420px;
    background: linear-gradient(180deg, var(--ghost-bottom), var(--ghost-top) 55%, var(--ghost-bottom));
  }
  .card-back .farmhouse-art { margin-top: 150px; }
  .card-back .ghost-art { height: 380px; bottom: 150px; }
  .website {
    position: absolute;
    z-index: 2;
    bottom: 70px;
    font-size: 32px;
    letter-spacing: 7px;
    color: var(--silver);
  }
</style>
</head>
<body>

  <section class="card card-front">
    <div class="farmhouse-art" role="img" aria-label="Woodcut illustration of the farmhouse in silver"></div>
    <div class="brand-name">Quillmere</div>
    <div class="brand-sub">FARM</div>

    <div class="person">
      <div class="person-name">AMOS TREBLECOTT</div>
      <div class="person-rule"></div>
      <div class="person-title">President/Owner</div>
    </div>

    <div class="ghost-art" role="img" aria-label="Faint woodcut illustration of the farmhouse"></div>

    <ul class="contact-list">
      <li class="contact-item">
        <svg class="contact-icon" viewBox="0 0 26 26"><rect x="1" y="1" width="24" height="24" rx="4" fill="#cfcfcf"/><rect x="6" y="8" width="14" height="10" fill="none" stroke="#0c0c0c" stroke-width="1.6"/><path d="M6 8 L13 14 L20 8" fill="none" stroke="#0c0c0c" stroke-width="1.6"/></svg>
        amos@quillmerefarm.com
      </li>
      <li class="contact-item">
        <svg class="contact-icon" viewBox="0 0 26 26"><rect x="1" y="1" width="24" height="24" rx="4" fill="#cfcfcf"/><rect x="9" y="5" width="8" height="16" rx="1.5" fill="none" stroke="#0c0c0c" stroke-width="1.6"/><circle cx="13" cy="18" r="1" fill="#0c0c0c"/></svg>
        413-555-0172
      </li>
      <li class="contact-item">
        <svg class="contact-icon" viewBox="0 0 26 26"><rect x="1" y="1" width="24" height="24" rx="4" fill="#cfcfcf"/><path d="M8 6 C7 10 10 17 17 20 L19 17 L16 15 L14 16 C12 15 11 14 10 12 L11 10 L9 7 Z" fill="#0c0c0c"/></svg>
        413-555-0148
      </li>
    </ul>

    <div class="social-row">
      <span class="social-handle"><span class="social-dot"></span>@quillmerefarm</span>
      <span class="social-handle"><span class="social-dot"></span>@quillmerefarmma</span>
    </div>
  </section>

  <section class="card card-back">
    <div class="farmhouse-art" role="img" aria-label="Woodcut illustration of the farmhouse in silver"></div>
    <div class="brand-name">Quillmere</div>
    <div class="brand-sub">FARM</div>
    <div class="ghost-art" role="img" aria-label="Faint woodcut illustration of the farmhouse"></div>
    <div class="website">QUILLMEREFARM.COM</div>
  </section>

</body>
</html>
```